Oil & Gas companies needs print design panels for Australia's biggest conference of 2016!

We need artwork design for 2 companies that are linked from Perth, Western Australia (KRV and Dulmora). Logos (in EPS format) have been attached.

Our websites (so that you can get a feel for what we do) are:
www.fenbrackworks.example
www.dulmora.example

We need two panels for our stand at the WIRLU conference in Brisbane. An image of the stand setup has been provided in the attached images. The panel artwork sizes required are:
1x 985mm x 2349mm h
1x 2349mm x 985mm h

A copy of the guidelines that need to be followed in order to have the artwork correctly displayed have also been attached.

WORDING FOR PANELS

KRV (logo) – panel
TAG LINE: KRV. Your Ally for Progress.
Completions and Commissioning,
Operational Readiness
Specialist Inspections,
Whatever your projects requirements,
Wherever you operate,
Whatever your schedule.
KRV keeps your venture moving forward.

Dulmora (logo) – panel
TAG LINE: Keep your assets under control.
Maintain plant safety.
Avoid unplanned downtime.
Comply with complex regulatory requirements.
Dulmora Hazardous Area and specialist inspection services.
Your Asset. Our Protection.

We need to x2 pics (from the ones supplied/or ones to do with Oil & Gas industry)

Target Market(s)

Conference
Oil & Gas professionals

Industry/Entity Type

Oil And Gas

Font styles to use
Sans Serif
Other font styles liked:
• DIN Offc

Requirements
Must have
• KRV & Dulmora Logo (one per panel)
• Must follow the attached guidelines provided from WIRLU.
• The KRV panel must be engaging and draw clients towards our stand as it is the first thing they will see when entering the conference.
• KRV & Dulmora colours:
• orange = #D76927, R-215 G-105 B-39, CMYK C-11.65 M-70.4 Y-100 K-1.52
• Blue = #21224B, R-33 G-34 B-75, CMYK C-95.65, M-92.65 Y-39.82, K40.01
Nice to have
• We would like to see some examples of faded pictures with wording more predominant.
• KRV:
• Completions and Commissioning - pop out/bold/stand out
• Operational Readiness - pop out/bold/stand out
• Inspections - pop out/bold/stand out
• Dulmora:
• Hazardous Area - pop out/bold/standout
Should not have
• Combined KRV/Dulmora panels - need to be separate

```html
<!DOCTYPE html>
<html lang="en">
<head>
<meta charset="utf-8">
<title>KRV – Your Ally for Progress</title>
<link rel="stylesheet" href="https://fonts.googleapis.com/css2?family=Barlow:wght@400;500;700&display=swap">
<style>
  :root {
    --brand-blue: #21224B;
    --brand-orange: #D76927;
    --white: #FFFFFF;
    --night-top: #2a3236;
    --night-mid: #1d2a2e;
    --plant-glow: #2f5a4a;
    --water: #1b1a1e;
    --band-shade: rgba(10, 10, 12, 0.72);
  }
  * { margin: 0; padding: 0; box-sizing: border-box; }
  html, body {
    width: 1200px;
    height: 2862px;
    overflow: hidden;
    background: var(--night-mid);
  }
  .panel {
    position: relative;
    width: 1200px;
    height: 2862px;
    overflow: hidden;
    font-family: "Barlow", sans-serif;
    color: var(--white);
  }
  .panel__photo {
    position: absolute;
    inset: 0;
    background:
      radial-gradient(ellipse 900px 260px at 70% 600px, rgba(190, 170, 150, 0.35), transparent 70%),
      radial-gradient(ellipse 700px 500px at 60% 1900px, rgba(80, 160, 120, 0.45), transparent 70%),
      radial-gradient(ellipse 500px 300px at 95% 1850px, rgba(200, 200, 190, 0.25), transparent 70%),
      linear-gradient(180deg, var(--night-top) 0%, var(--night-mid) 45%, var(--plant-glow) 68%, #1a2220 80%, var(--water) 100%);
  }
  .brand {
    position: absolute;
    top: 230px;
    left: 0;
    width: 100%;
    text-align: center;
    font-weight: 700;
    font-size: 330px;
    line-height: 1;
    letter-spacing: 24px;
    color: var(--white);
  }
  .headline {
    position: absolute;
    top: 718px;
    left: 254px;
    font-weight: 700;
    font-size: 172px;
    line-height: 181px;
    letter-spacing: 1px;
    text-transform: uppercase;
  }
  .services-band {
    position: absolute;
    top: 2290px;
    left: 0;
    width: 100%;
    height: 137px;
    background: var(--band-shade);
  }
  .services {
    position: absolute;
    top: 2304px;
    left: 0;
    width: 100%;
    text-align: center;
    font-weight: 500;
    font-size: 39px;
    line-height: 49px;
  }
  .services__promise {
    position: absolute;
    top: 2618px;
    left: 0;
    width: 100%;
    text-align: center;
    font-weight: 700;
    font-size: 38px;
  }
  .footer {
    position: absolute;
    left: 0;
    bottom: 0;
    width: 100%;
    height: 133px;
    background: var(--brand-orange);
    border-top: 4px solid var(--white);
    display: flex;
    align-items: center;
    justify-content: center;
  }
  .footer__url {
    font-weight: 700;
    font-size: 64px;
    letter-spacing: 1px;
    color: var(--white);
  }
</style>
</head>
<body>
  <main class="panel">
    <div class="panel__photo" role="img" aria-label="Night view of an oil refinery with a striped chimney stack, lit processing towers and reflections on the water"></div>

    <div class="brand">KRV</div>

    <h1 class="headline">Your<br>Ally<br>For<br>Progress</h1>

    <div class="services-band"></div>
    <p class="services">
      Completions and Commissioning,<br>
      Operational Readiness,<br>
      Specialist Inspections,<br>
      Whatever your projects requirements,<br>
      Wherever you operate,<br>
      Whatever your schedule.
    </p>
    <p class="services__promise">KRV keeps your venture moving forward!</p>

    <footer class="footer">
      <span class="footer__url">www.fenbrackworks.example</span>
    </footer>
  </main>
</body>
</html>
```